International business needs a web page design

We need a web page design for a new service that our new "sub-company" of our existing company will offer. We are based in Denmark, and our new "sub-company" is called 'Velkari'. The service we offer is automated server configuration and In-Depth monitoring, and optional operations support. Our monitoring has a lot of graphs (like those seen here: https://velkari.example/ with either black or white background ) and the website needs to communicate a sense of Security/safety and that our customers can relax, because we have the full overview of their service and servers. The website should not be with black background.

We deliver low price, high quality and professional operations - which we can do, because we automate it and have people with 15+ years of experience doing so.

We have attached :
a file with our logo : velkari
a file showing the content of the frontage : frontpage
a file showing the content of the user page(for logged in users) : User page
a file showing the pop-up dialog "page" : CallToAction_route
a file showing the 3-steps for the frontpage : 3-step for frontpage

Target Market(s)

Chief Technological officers (CTO's) and Developers (small business, run by developers) - who needs professional IT operations.

Industry/Entity Type

Business

Coding

Coded - Design and coding required

Number of Pages Required

3 page

Requirements
Must have
• Frontpage :
• A lot of visualization(some with people too) rather than a lot of text
• A short, describing text on front page telling what people get
• 3 steps showing people how it works. (Could be presented in a video placed on top of a big front image or perhaps with all 3 steps/pictures shown at the same time or perhaps in a completely different way).
Nice to have
• A big front image(perhaps a person with a cellphone showing graphs and a "all okay" message) with a text and the 3-steps pictures/or video on top of it
• 3 boxes under the front image/top of the site showing what benefits people get from the service
Should not have
• Not a black/dark site

```html
<!DOCTYPE html>
<html lang="en">
<head>
<meta charset="utf-8">
<title>Velkari – Instant server setup and in-depth monitoring</title>
<link href="https://fonts.googleapis.com/css2?family=Open+Sans:wght@300;400;600;700&display=swap" rel="stylesheet">
<style>
:root{
  --blue:#0a8fd0;
  --blue-dark:#0678b2;
  --green:#5cbc3c;
  --ink:#2b2f33;
  --grey:#777d82;
  --pale:#eef1f3;
  --white:#ffffff;
  --footer:#33393d;
  --footer-text:#b8bec2;
}
*{box-sizing:border-box;margin:0;padding:0}
html,body{width:768px;height:1200px;overflow:hidden}
body{font-family:"Open Sans",Arial,sans-serif;color:var(--ink);background:var(--white);position:relative}
.abs{position:absolute}
a{color:inherit;text-decoration:none}

/* header */
.site-header{left:0;top:0;width:768px;height:48px;background:var(--white)}
.brand{left:120px;top:5px;display:flex;align-items:center;gap:7px}
.brand-dot{width:37px;height:37px;border-radius:50%;background:var(--blue)}
.brand-name{font-size:25px;font-weight:600;color:var(--ink);letter-spacing:-.3px}
.main-nav a{position:absolute;top:16px;font-size:8px;color:#7a7f84;letter-spacing:.2px;white-space:nowrap}
.main-nav .active{color:var(--blue)}
.login-btn{left:565px;top:12px;width:39px;height:20px;background:var(--green);color:var(--white);font-size:7px;font-weight:600;display:flex;align-items:center;justify-content:center}
.header-social{left:617px;top:19px;display:flex;gap:4px}
.header-social span{width:7px;height:7px;border-radius:50%;background:#8a8f93}

/* hero */
.hero{left:0;top:48px;width:768px;height:337px;background:var(--blue);overflow:hidden}
.hero-backdrop{left:0;top:0;width:330px;height:337px;background:linear-gradient(160deg,#0a8fd0 0%,#0a8fd0 30%,#0780be 70%,#0a8fd0 100%)}
.hero-photo{left:310px;top:0;width:458px;height:337px;background:linear-gradient(120deg,#0a8fd0 0%,#3aa3d8 35%,#c8d8e6 60%,#e7eef4 100%)}
.play-ring{left:404px;top:212px;width:32px;height:32px;border:2px solid var(--white);border-radius:50%;display:flex;align-items:center;justify-content:center}
.hero-title{left:122px;top:58px;color:var(--white);font-size:16.5px;font-weight:700;line-height:21px;letter-spacing:.3px}
.hero-points{left:121px;top:112px;list-style:none;color:var(--white);font-size:9.5px}
.hero-points li{display:flex;align-items:center;gap:7px;height:18.5px}
.hero-cta{left:120px;top:172px;width:185px;height:25px;background:var(--green);color:var(--white);font-size:7.5px;font-weight:600;display:flex;align-items:center;justify-content:center;letter-spacing:.1px}
.bullet{width:10px;height:10px;flex:none}

/* benefits */
.benefits{left:0;top:385px;width:768px;height:189px;background:var(--pale)}
.benefit{top:-10px;width:170px;text-align:center}
.benefit-icon{width:88px;height:88px;margin:0 auto;border-radius:50%;background:var(--pale);display:flex;align-items:flex-start;justify-content:center}
.benefit-icon span{margin-top:8px;width:76px;height:76px;border-radius:50%;background:var(--blue);display:flex;align-items:center;justify-content:center}
.benefit h3{font-size:11px;font-weight:400;color:var(--ink);height:30px;display:flex;align-items:flex-end;justify-content:center;line-height:14px;margin-top:3px}
.benefit p{font-size:7px;line-height:11.6px;color:var(--grey);margin-top:8px}

/* demo */
.demo{left:0;top:574px;width:768px;height:221px;background:var(--white)}
.demo-lead{left:120px;top:17px;font-size:14.5px;font-weight:300}
.demo-title{left:120px;top:38px;font-size:18.5px;font-weight:600;letter-spacing:.2px}
.demo-title em{font-style:normal;color:var(--blue)}
.demo-list{list-style:none;font-size:7px;line-height:11.3px;color:var(--grey)}
.demo-list li{display:flex;gap:4px;margin-bottom:10px;height:22px}
.demo-list .bullet{width:8px;height:8px;margin-top:1.5px}
.demo-btn{left:120px;top:173px;width:84px;height:26px;background:var(--green);color:var(--white);font-size:7.5px;font-weight:600;display:flex;align-items:center;justify-content:center}
.demo-photo{left:415px;top:0;width:353px;height:221px;background:linear-gradient(135deg,#b9a894 0%,#8a7866 35%,#3b4f6e 65%,#7d95b4 100%)}

/* testimonials */
.reviews{left:0;top:795px;width:768px;height:264px;background:var(--pale)}
.reviews-title{left:0;top:22px;width:768px;text-align:center;font-size:17.5px;font-weight:600;letter-spacing:.2px}
.quote-card{left:171px;top:71px;width:196px;height:134px;background:var(--blue);color:var(--white);font-size:9px;line-height:15px;padding:21px 22px 0;text-align:justify}
.quote-tail{left:250px;top:205px}
.avatar{left:193px;top:181px;width:59px;height:59px;border-radius:50%;border:3px solid var(--white);background:radial-gradient(circle at 50% 40%,#c99a7c,#8d5e45 70%,#a33a35)}
.reviewer{font-size:7.5px;line-height:11px}
.reviewer b{font-weight:600;color:var(--ink);display:block}
.reviewer span{color:var(--blue-dark);font-size:6.8px}
.video-card{left:401px;top:71px;width:196px;height:134px;background:linear-gradient(135deg,#8c8a80,#c7b69b 50%,#6e6a61)}
.video-play{left:80px;top:48px;width:38px;height:38px;border-radius:50%;background:var(--white);display:flex;align-items:center;justify-content:center}
.arrow{top:130px}

/* footer */
.site-footer{left:0;top:1059px;width:768px;height:141px;background:var(--footer)}
.footer-heading{left:120px;top:30px;font-size:11px;color:var(--blue);font-weight:400;letter-spacing:.2px}
.footer-about{left:120px;top:50px;width:175px;font-size:6.8px;line-height:11.6px;color:var(--footer-text)}
.footer-brand{left:320px;top:28px;display:flex;align-items:center;gap:6px;opacity:.55}
.footer-brand .brand-dot{width:34px;height:34px;background:#7d8387}
.footer-brand .brand-name{font-size:23px;color:#7d8387}
.footer-nav{left:326px;top:72px;display:flex;gap:12px;font-size:7px;color:var(--footer-text)}
.footer-cta{left:314px;top:91px;width:162px;height:20px;background:var(--blue);color:var(--white);font-size:6.8px;font-weight:600;display:flex;align-items:center;justify-content:center}
.contact{left:502px;font-size:6.8px;color:var(--footer-text);display:flex;align-items:center;gap:7px}
.footer-social{left:504px;top:82px;display:flex;gap:6px}
.footer-social span{width:13px;height:13px;border-radius:50%;border:1px solid var(--blue)}
.copyright{left:502px;top:105px;font-size:6.8px;color:var(--footer-text)}
.copyright a{color:var(--blue)}
</style>
</head>
<body>

<header class="site-header abs">
  <a class="brand abs" href="https://velkari.example/"><span class="brand-dot"></span><span class="brand-name">Velkari</span></a>
  <nav class="main-nav">
    <a class="active" href="#" style="left:367px">HOME</a>
    <a href="#" style="left:409px">SERVICES</a>
    <a href="#" style="left:461px">ABOUT US</a>
    <a href="#" style="left:518px">SUPPORT</a>
  </nav>
  <a class="login-btn abs" href="#">LOGIN</a>
  <div class="header-social abs" aria-label="Social links"><span></span><span></span><span></span></div>
</header>

<section class="hero abs">
  <div class="hero-backdrop abs" role="img" aria-label="Faint blue background graphic of rising chart lines"></div>
  <div class="hero-photo abs" role="img" aria-label="Smiling man in shirt and red tie pointing at a laptop showing monitoring dashboards"></div>
  <div class="play-ring abs" aria-label="Play video">
    <svg width="12" height="14" viewBox="0 0 12 14"><polyline points="3,1 9,7 3,13" fill="none" stroke="#fff" stroke-width="2"/></svg>
  </div>
  <h1 class="hero-title abs">INSTANT SERVER SETUP AND<br>IN-DEPTH MONITORING</h1>
  <ul class="hero-points abs">
    <li><svg class="bullet" viewBox="0 0 10 10"><circle cx="5" cy="5" r="4.3" fill="none" stroke="#fff" stroke-width="1"/><polyline points="4,3 6,5 4,7" fill="none" stroke="#fff" stroke-width="1"/></svg>Lorem ipsum dolor sit amet, consectetur adipiscing elit.</li>
    <li><svg class="bullet" viewBox="0 0 10 10"><circle cx="5" cy="5" r="4.3" fill="none" stroke="#fff" stroke-width="1"/><polyline points="4,3 6,5 4,7" fill="none" stroke="#fff" stroke-width="1"/></svg>Proin efficitur ipsum non condimentum tincidunt.</li>
    <li><svg class="bullet" viewBox="0 0 10 10"><circle cx="5" cy="5" r="4.3" fill="none" stroke="#fff" stroke-width="1"/><polyline points="4,3 6,5 4,7" fill="none" stroke="#fff" stroke-width="1"/></svg>Ut sollicitudin lorem commodo est.</li>
  </ul>
  <a class="hero-cta abs" href="#">CLICK TO GET INSTANT SERVER SETUP NOW</a>
</section>

<section class="benefits abs">
  <div class="benefit abs" style="left:116px">
    <div class="benefit-icon"><span>
      <svg width="36" height="36" viewBox="0 0 36 36" fill="#fff"><path d="M28 6c-6 0-12 4-15 10l-4 1-4 5 6 1 3 3 1 6 5-4 1-4c6-3 10-9 10-15z"/><circle cx="22" cy="13" r="2.5" fill="#0a8fd0"/><path d="M9 24l-4 7 7-4z"/></svg>
    </span></div>
    <h3>It is fast and easy</h3>
    <p>Ras facilisis pulvinar tincidunt. Maecenas bibendum varius suscipit. Quisque sit amet quam a est ornare interdum. Duis lacus mauris, consequat at massa non, posuere consequat dolor.</p>
  </div>
  <div class="benefit abs" style="left:299px">
    <div class="benefit-icon"><span>
      <svg width="38" height="38" viewBox="0 0 38 38"><path d="M19 3l4 3 5-1 2 5 5 2-1 5 3 4-3 4 1 5-5 2-2 5-5-1-4 3-4-3-5 1-2-5-5-2 1-5-3-4 3-4-1-5 5-2 2-5 5 1z" fill="#fff"/><circle cx="19" cy="19" r="10" fill="none" stroke="#0a8fd0" stroke-width="2"/><polyline points="14,19 18,23 25,15" fill="none" stroke="#0a8fd0" stroke-width="2.5"/></svg>
    </span></div>
    <h3>Relax &amp; Rest Assured</h3>
    <p>Ras facilisis pulvinar tincidunt. Maecenas bibendum varius suscipit. Quisque sit amet quam a est ornare interdum. Duis lacus mauris, consequat at massa non, posuere consequat dolor.</p>
  </div>
  <div class="benefit abs" style="left:481px">
    <div class="benefit-icon"><span>
      <svg width="38" height="38" viewBox="0 0 38 38" fill="#fff"><path d="M20 20c-6-4-9-7-9-10a4.5 4.5 0 0 1 9-1 4.5 4.5 0 0 1 9 1c0 3-3 6-9 10z"/><path d="M4 24h5l6 2h6a2 2 0 0 1 0 4h-6 7l9-5a2 2 0 0 1 2 3l-10 7H9l-5-2z"/></svg>
    </span></div>
    <h3>You'll love your<br>detailed performance graph</h3>
    <p>Ras facilisis pulvinar tincidunt. Maecenas bibendum varius suscipit. Quisque sit amet quam a est ornare interdum. Duis lacus mauris, consequat at massa non, posuere consequat dolor.</p>
  </div>
</section>

<section class="demo abs">
  <p class="demo-lead abs">Sign Up to</p>
  <h2 class="demo-title abs">GET THE <em>FREE</em> DEMO</h2>
  <ul class="demo-list abs" style="left:120px;top:73px;width:120px">
    <li><svg class="bullet" viewBox="0 0 10 10"><circle cx="5" cy="5" r="4.3" fill="none" stroke="#0a8fd0"/><polyline points="4,3 6,5 4,7" fill="none" stroke="#0a8fd0"/></svg><span>Cras facilisis pulvinar tincidunt. Maecenas bibendum varius</span></li>
    <li><svg class="bullet" viewBox="0 0 10 10"><circle cx="5" cy="5" r="4.3" fill="none" stroke="#0a8fd0"/><polyline points="4,3 6,5 4,7" fill="none" stroke="#0a8fd0"/></svg><span>Cras facilisis pulvinar tincidunt. Maecenas bibendum varius</span></li>
    <li><svg class="bullet" viewBox="0 0 10 10"><circle cx="5" cy="5" r="4.3" fill="none" stroke="#0a8fd0"/><polyline points="4,3 6,5 4,7" fill="none" stroke="#0a8fd0"/></svg><span>Cras facilisis pulvinar tincidunt. Maecenas bibendum varius</span></li>
  </ul>
  <ul class="demo-list abs" style="left:251px;top:73px;width:140px">
    <li><svg class="bullet" viewBox="0 0 10 10"><circle cx="5" cy="5" r="4.3" fill="none" stroke="#0a8fd0"/><polyline points="4,3 6,5 4,7" fill="none" stroke="#0a8fd0"/></svg><span>Quisque sit amet quam a est ornare interdum.</span></li>
    <li><svg class="bullet" viewBox="0 0 10 10"><circle cx="5" cy="5" r="4.3" fill="none" stroke="#0a8fd0"/><polyline points="4,3 6,5 4,7" fill="none" stroke="#0a8fd0"/></svg><span>Duis lacus mauris, consequat at massa non, posuere consequat dolor.</span></li>
    <li><svg class="bullet" viewBox="0 0 10 10"><circle cx="5" cy="5" r="4.3" fill="none" stroke="#0a8fd0"/><polyline points="4,3 6,5 4,7" fill="none" stroke="#0a8fd0"/></svg><span>Proin sit amet dolor eu mauris mattis.</span></li>
  </ul>
  <a class="demo-btn abs" href="#">SIGN UP NOW!</a>
  <div class="demo-photo abs" role="img" aria-label="Person in jeans holding a tablet showing monitoring graphs"></div>
</section>

<section class="reviews abs">
  <h2 class="reviews-title abs">WHY PEOPLE LOVE US</h2>
  <svg class="arrow abs" style="left:120px" width="26" height="46" viewBox="0 0 26 46"><polyline points="24,1 2,23 24,45" fill="none" stroke="#b5bcc1" stroke-width="1.5"/></svg>
  <svg class="arrow abs" style="left:622px" width="26" height="46" viewBox="0 0 26 46"><polyline points="2,1 24,23 2,45" fill="none" stroke="#b5bcc1" stroke-width="1.5"/></svg>
  <blockquote class="quote-card abs">“Cras facilisis pulvinar tincidunt. Maecenas bibendum varius suscipit. Quisque sit amet quam a est ornare interdum. Duis lacus mauris, cons equat at massa non,</blockquote>
  <svg class="quote-tail abs" width="14" height="14" viewBox="0 0 14 14"><polygon points="0,0 14,0 4,14" fill="#0a8fd0"/></svg>
  <div class="avatar abs" role="img" aria-label="Portrait photo of John Smith"></div>
  <p class="reviewer abs" style="left:270px;top:213px"><b>JOHN SMITH</b><span>New York, A Lorem Ipsum Co.</span></p>
  <div class="video-card abs" role="img" aria-label="Video testimonial still of a smiling blonde woman">
    <span class="video-play abs"><svg width="14" height="16" viewBox="0 0 14 16"><polygon points="2,0 14,8 2,16" fill="#0a8fd0"/></svg></span>
  </div>
  <p class="reviewer abs" style="left:407px;top:213px"><b>MISS RITA</b><span>London Heathrow, A Lorem Ipsum Co.</span></p>
</section>

<footer class="site-footer abs">
  <h4 class="footer-heading abs">ABOUT VELKARI</h4>
  <p class="footer-about abs">Cras facilisis pulvinar tincidunt. Maecenas bibendum varius suscipit. Quisque sit amet quam a est ornare interdum. Duis lacus mauris, consequat at massa non, posuere consequat dolor. Proin sit amet dolor eu mauris mattis tempus eget sed risus.</p>
  <div class="footer-brand abs"><span class="brand-dot"></span><span class="brand-name">Velkari</span></div>
  <nav class="footer-nav abs"><a href="#">Home</a><a href="#">Services</a><a href="#">About Us</a><a href="#">Support</a></nav>
  <a class="footer-cta abs" href="#">CLICK TO GET INSTANT SERVER SETUP NOW</a>
  <p class="contact abs" style="top:46px"><svg width="8" height="10" viewBox="0 0 8 10"><path d="M4 0a3.5 3.5 0 0 1 3.5 3.5C7.5 6 4 10 4 10S.5 6 .5 3.5A3.5 3.5 0 0 1 4 0z" fill="#0a8fd0"/><circle cx="4" cy="3.5" r="1.3" fill="#33393d"/></svg>150, Lorem Ipsum, Dolor Sit, United State</p>
  <p class="contact abs" style="top:64px"><svg width="8" height="7" viewBox="0 0 8 7"><rect width="8" height="7" fill="#0a8fd0"/><polyline points="0,0 4,4 8,0" fill="none" stroke="#33393d"/></svg>support@velkari.example</p>
  <div class="footer-social abs" aria-label="Social links"><span></span><span></span><span></span></div>
  <p class="copyright abs">Copyright 2014 by <a href="https://velkari.example/">velkari.example</a></p>
</footer>

</body>
</html>
```